Verdant Row

Currently www.verdantrow-example.com. This site was designed with a generic templet. However it is functional. I'm looking for a fun, fresh, and professional design. I also need help getting the XML for Searchly and Findo. I'm not a web designer and need help. I do not like my current sites narrow width.
Updates

All and all I'm liking the designs. The earlier ones seem better. Some seem that they are just taking my images and inputing them into a templet. I could have done that. The pictures are nice. Please keep in mind, functionality and updates. Please help us show our customers our how we are different. Safe Reliable Responsible are the key fundamentals, inside of these fundamentals show that were are customer service specialized. We are, Licensed, Insured, Drug Screened, Criminally Screened. Seems that people are putting up nice pictures but not capturing our values. Please help us market us on our website. Show our prospective customers why we are better, how we differentiate ourself from the competitors. Why choose us? Our flyers and cards are designed to drive our prospective customers to the website. If it looks identical with no pazaz like the card, then the marketing chain failed. I included our cards to help guide the thought process of our company. The link below is a feature I would love to have. This may be another project itself. I'm not sure if PX is the place to accomplish it. Below is a link for people to estimate there lawns with globe viewer. I would like to give a range of estimates using this technology. I have no clue how to accomplish it. If anyone knows how to who could do this, Please let me know. https://www.yardquoter-example.com/showOrder/MOWLAWN/propertyDetails

Target Market(s)

We target residential customers 30-80 yr old. We also are expanding and placing a special emphasis on Business accounts. The main service is a mowing and landscape maintenance. Should be the main focus of the site.

Industry/Entity Type

Searchly

Coding

Coded - Design and coding required

Font styles to use
Sans Serif

Requirements
Must have
• I want this site to be fun and colorful. It still needs to be professional looking as not to deter business accounts. If you use photos, they must reflect Florida lawn. Note the architecture the homes, grass type, types of plants.
Should not have
• My current site is ok. I use it just as a

```html
<!DOCTYPE html>
<html lang="en">
<head>
<meta charset="utf-8">
<title>Verdant Row – Lawn Care</title>
<link rel="stylesheet" href="https://fonts.googleapis.com/css2?family=Montserrat:wght@300;400;500;600;700&display=swap">
<style>
:root{
  --green:#6aa51a;
  --green-dark:#5a9312;
  --green-text:#6aab2c;
  --field:#72ad1f;
  --red:#ee4732;
  --red-soft:#f26a52;
  --grey-bg:#f4f4f4;
  --text:#6f6f6f;
  --dark:#3a3a3a;
  --white:#ffffff;
}
*{margin:0;padding:0;box-sizing:border-box}
html,body{width:1008px;height:1200px;overflow:hidden;background:var(--white)}
body{font-family:"Montserrat",Arial,sans-serif;color:var(--text);position:relative}
.abs{position:absolute}

/* header */
.site-header{position:absolute;left:0;top:0;width:1008px;height:105px;background:var(--white)}
.brand{position:absolute;left:72px;top:30px;display:flex;align-items:center;gap:8px}
.brand-dot{width:22px;height:22px;border-radius:50%;background:var(--red)}
.brand-name{font-size:27px;font-weight:700;color:var(--green)}
.tagline{position:absolute;left:285px;top:18px;font-size:11.5px;line-height:13px;color:#555;width:130px}
.call{position:absolute;left:285px;top:52px}
.call-label{font-size:11px;font-weight:700;color:var(--green);display:inline-block;width:70px}
.call-digits{font-size:10px;color:#999;letter-spacing:6px}
.call-number{font-size:15px;color:var(--red);letter-spacing:.5px;margin-top:-2px}
.top-bar{position:absolute;left:463px;top:0;width:472px;height:26px;background:var(--green);border-radius:0 0 6px 6px;color:var(--white);font-size:9.5px;display:flex;align-items:center;justify-content:center;gap:10px;letter-spacing:.3px}
.main-nav{position:absolute;top:65px;left:452px;font-size:14px;color:#555}
.main-nav a{position:absolute;white-space:nowrap;color:inherit;text-decoration:none}
.main-nav .active{color:var(--red);font-weight:600}

/* hero */
.hero{position:absolute;left:0;top:105px;width:1008px;height:342px;background:
  radial-gradient(ellipse at 20% 40%,#e9d23a 0 8%,transparent 22%),
  radial-gradient(ellipse at 60% 75%,#b7766a 0 9%,transparent 20%),
  radial-gradient(ellipse at 85% 85%,#d9d2c8 0 12%,transparent 26%),
  linear-gradient(180deg,#4d7a2a 0%,#5f8f33 45%,#6ea03a 80%,#8ab54c 100%)}
.hero-arrow{position:absolute;top:148px;width:42px;height:42px;border-radius:50%;background:rgba(255,255,255,.85)}
.hero-arrow.prev{left:-20px}
.hero-arrow.next{right:-20px}
.hero-arrow svg{position:absolute;top:13px}
.hero-arrow.prev svg{left:22px}
.hero-arrow.next svg{left:10px}
.hero-banner{position:absolute;left:0;top:261px;width:1008px;height:81px;background:linear-gradient(90deg,rgba(238,71,50,0) 12%,rgba(238,71,50,.85) 32%,rgba(238,71,50,.9) 50%,rgba(238,71,50,.85) 68%,rgba(238,71,50,0) 88%);text-align:center;color:var(--white)}
.hero-banner h1{font-weight:400;font-size:27px;letter-spacing:.5px;margin-top:12px}
.hero-banner p{font-size:15px;font-weight:300;margin-top:-1px}
.hero-pointer{position:absolute;left:470px;top:447px;z-index:2}

/* intro */
.intro{position:absolute;left:0;top:447px;width:1008px;height:190px;background:var(--grey-bg)}
.intro-curve{position:absolute;left:0;top:592px}
.intro-lead{position:absolute;left:140px;top:43px;width:728px;text-align:center;font-size:16.5px;line-height:20px;color:var(--green-text)}
.intro-body{position:absolute;left:70px;top:103px;width:868px;text-align:center;font-size:10.3px;line-height:13px;color:#777}

/* services */
.services-title{position:absolute;left:0;top:662px;width:1008px;text-align:center;font-size:23px;font-weight:300;color:#777;letter-spacing:.5px}
.service{position:absolute;width:280px}
.service-icon{position:absolute;left:0;top:0;width:60px;height:52px}
.service h3{position:absolute;left:74px;top:0;font-size:13.5px;font-weight:400;color:var(--red);white-space:nowrap}
.service p{position:absolute;left:74px;top:21px;width:200px;font-size:10.5px;line-height:14.5px;color:#888}
.service .readmore{position:absolute;left:74px;top:74px;font-size:9.5px;font-weight:700;color:var(--green);letter-spacing:.3px;text-decoration:none}

/* newsletter */
.newsletter{position:absolute;left:0;top:943px;width:1008px;height:185px}
.newsletter svg.bg{position:absolute;left:0;top:0}
.nl-kicker{position:absolute;left:0;top:35px;width:1008px;text-align:center;font-size:11px;font-weight:700;color:var(--white);letter-spacing:.3px}
.nl-title{position:absolute;left:0;top:50px;width:1008px;text-align:center;font-size:23px;font-weight:400;color:var(--white)}
.nl-field{position:absolute;top:99px;width:220px;height:47px;border:1px solid #a9d66a;background:var(--field);color:var(--white);font-size:12px;padding:16px 14px}
.nl-submit{position:absolute;left:765px;top:99px;width:164px;height:48px;background:var(--red);border:1px solid #fff;color:var(--white);font-size:10.5px;font-weight:700;text-align:center;line-height:46px;letter-spacing:.3px}

/* footer */
.site-footer{position:absolute;left:0;top:1129px;width:1008px;height:71px;background:var(--dark);border-top:2px solid #cfe0b6;color:#e6e6e6;font-size:10.5px}
.footer-left{position:absolute;left:71px;top:32px;white-space:nowrap}
.footer-nav{position:absolute;left:543px;top:34px;white-space:nowrap}
.sep{color:#999;margin:0 10px}
.social{position:absolute;top:28px;width:18px;height:18px;border-radius:50%;background:#6d6d6d}
</style>
</head>
<body>

<header class="site-header">
  <div class="brand"><span class="brand-dot"></span><span class="brand-name">Verdant Row</span></div>
  <p class="tagline">For a refreshing lawn care experience</p>
  <div class="call">
    <div><span class="call-label">call</span><span class="call-digits">9273</span></div>
    <div class="call-number">800-555-YARD</div>
  </div>
  <div class="top-bar">
    <span>TOLL FREE&nbsp; 800-555-0142</span><span>| LANDLINE&nbsp; 386-555-0190</span><span>&nbsp;| &nbsp;LOGIN</span><span>| &nbsp;GET REGISTERED</span>
  </div>
  <nav class="main-nav">
    <a class="active" style="left:0">Home</a>
    <a style="left:95px">About</a>
    <a style="left:192px">Services</a>
    <a style="left:298px">Estimate</a>
    <a style="left:403px">Contact Us</a>
  </nav>
</header>

<section class="hero" role="img" aria-label="Photo of a landscaped garden with yellow lilies, flower beds, boulders and a curved stone path">
  <div class="hero-arrow prev"><svg width="10" height="16" viewBox="0 0 10 16"><path d="M8 2 2 8l6 6" fill="none" stroke="#ee4732" stroke-width="3"/></svg></div>
  <div class="hero-arrow next"><svg width="10" height="16" viewBox="0 0 10 16"><path d="M2 2l6 6-6 6" fill="none" stroke="#ee4732" stroke-width="3"/></svg></div>
  <div class="hero-banner">
    <h1>WELCOME TO VERDANT ROW</h1>
    <p>“Your Year Around Lawn Care Solution”</p>
  </div>
</section>
<svg class="hero-pointer abs" width="68" height="18" viewBox="0 0 68 18"><path d="M0 0h68L34 18z" fill="#ef5a40"/></svg>

<section class="intro">
  <p class="intro-lead">Verdant Row is SAFE, Reliable, and Responsible. We make sure that all of our lawn care professionals are licensed, insured, drug-free, background checks completed and legally eligible to work.</p>
  <p class="intro-body">Verdant Row offers convenient online bill pay, we accepts credit cards, and we pride ourselves with a great customer service department.If you are tired of lawn service companies that deliver poor quality, never call you back, have lousy communication skills, and are generally unprofessional and unreliable please consider giving Verdant Row a try !</p>
</section>
<svg class="intro-curve" width="1008" height="50" viewBox="0 0 1008 50"><path d="M0 0Q504 58 1008 0V50H0z" fill="#fff"/></svg>

<h2 class="services-title">OUR SERVICES</h2>

<article class="service" style="left:72px;top:718px">
  <svg class="service-icon" viewBox="0 0 60 52"><path d="M2 4l10 4 12 22h24l-4 10H22" fill="none" stroke="#ee4732" stroke-width="3"/><circle cx="26" cy="44" r="6" fill="#ee4732"/><circle cx="48" cy="40" r="3" fill="#ee4732"/><circle cx="55" cy="34" r="2" fill="#ee4732"/></svg>
  <h3>Lawn Care</h3>
  <p>Lorem ipsum dolor sit amet, consectetuer adipiscing elit, sed diam nonummy</p>
  <a class="readmore">READMORE &#8250;</a>
</article>
<article class="service" style="left:367px;top:718px">
  <svg class="service-icon" viewBox="0 0 60 52"><path d="M8 18c0 14 8 20 16 20s16-6 16-20l-6 6-4-12-6 8-6-8-4 12z" fill="#ee4732"/><path d="M24 38v12" stroke="#ee4732" stroke-width="3"/></svg>
  <h3>Flower Bed Maintenance</h3>
  <p>Lorem ipsum dolor sit amet, consectetuer adipiscing elit, sed diam nonummy</p>
  <a class="readmore">READMORE &#8250;</a>
</article>
<article class="service" style="left:662px;top:718px">
  <svg class="service-icon" viewBox="0 0 60 52"><path d="M6 2l14 26" stroke="#ee4732" stroke-width="4"/><path d="M14 28h28l8 8v6H12z" fill="#ee4732"/><circle cx="20" cy="44" r="6" fill="#ee4732" stroke="#fff" stroke-width="2"/><circle cx="44" cy="44" r="6" fill="#ee4732" stroke="#fff" stroke-width="2"/></svg>
  <h3>Trimming and Pruning</h3>
  <p>Lorem ipsum dolor sit amet, consectetuer adipiscing elit, sed diam nonummy</p>
  <a class="readmore">READMORE &#8250;</a>
</article>

<article class="service" style="left:72px;top:822px">
  <svg class="service-icon" viewBox="0 0 60 52"><path d="M0 34h14l14 6h22c4 0 4 6 0 6H20l-6-2H0z" fill="#ee4732"/><path d="M30 32c-8-4-10-12-6-16 6 2 8 10 6 16zM32 30c2-10 12-16 22-16-2 10-12 16-22 16z" fill="#ee4732"/></svg>
  <h3>Plant and Shrub Installation</h3>
  <p>Lorem ipsum dolor sit amet, consectetuer adipiscing elit, sed diam nonummy</p>
  <a class="readmore">READMORE &#8250;</a>
</article>
<article class="service" style="left:367px;top:822px">
  <svg class="service-icon" viewBox="0 0 60 52"><path d="M40 10l-20 20 4 4-8 14 6 2 8-14 4 2 18-20z" fill="#ee4732"/><path d="M44 6l4-4M50 10l6-2M46 4l2-4" stroke="#ee4732" stroke-width="1.5"/></svg>
  <h3>Power Washing</h3>
  <p>Lorem ipsum dolor sit amet, consectetuer adipiscing elit, sed diam nonummy</p>
  <a class="readmore">READMORE &#8250;</a>
</article>
<article class="service" style="left:662px;top:822px">
  <svg class="service-icon" viewBox="0 0 60 52"><rect x="4" y="26" width="26" height="12" fill="#ee4732"/><rect x="16" y="18" width="12" height="10" fill="#ee4732"/><circle cx="10" cy="42" r="7" fill="#ee4732" stroke="#fff" stroke-width="2"/><circle cx="28" cy="44" r="5" fill="#ee4732" stroke="#fff" stroke-width="2"/><path d="M30 26l10-14" stroke="#ee4732" stroke-width="3"/><circle cx="44" cy="10" r="9" fill="#ee4732"/></svg>
  <h3>Tree Trimming/Removal</h3>
  <p>Lorem ipsum dolor sit amet, consectetuer adipiscing elit, sed diam nonummy</p>
  <a class="readmore">READMORE &#8250;</a>
</article>

<section class="newsletter">
  <svg class="bg" width="1008" height="185" viewBox="0 0 1008 185"><path d="M0 32Q504 -30 1008 32V185H0z" fill="#6aa51a"/></svg>
  <p class="nl-kicker">STAY IN TOUCH</p>
  <h2 class="nl-title">Get updates from VERDANT ROW</h2>
  <div class="nl-field" style="left:74px">First name</div>
  <div class="nl-field" style="left:305px">Last name</div>
  <div class="nl-field" style="left:535px">Email Address</div>
  <div class="nl-submit">SUBMIT</div>
</section>

<footer class="site-footer">
  <div class="footer-left">VERDANT ROW © 2014<span class="sep">|</span>Terms &amp; Services<span class="sep">|</span>Privacy Policy</div>
  <div class="footer-nav">Home<span class="sep">|</span>About<span class="sep">|</span>Services<span class="sep">|</span>Estimate<span class="sep">|</span>Contact Us</div>
  <span class="social" style="left:869px"></span>
  <span class="social" style="left:892px"></span>
  <span class="social" style="left:915px"></span>
</footer>

</body>
</html>
```